Professional, Elegant, Modern and Playful Appointment Card Design for an Orthodontist (Dentist)

We need an appointment card design for an orthodontist (Dentist).
We would like to see designs that are elegant, but also playful.
The designs and colors should be in harmony with the existing logo (uploaded).
The font of the logo text is also uploaded. You don't need to use the same font, but the used fonts have to be in harmony with the font used in the logo.
The colors used have to be in harmony with the logo.
Size: 85mm x 130mm
The appointment card will be folded vertically in the middle (folded size: 85mm x 65mm). Please design both outer sides.
The appointments will be printed on the inner side (see uploaded "appointment card.pdf"). Please design the background on the inner side, but make it discreet.
Following information have to be present:
- Logo
- Text:
Kieferorthopädie Birkenhain
Dr. med. dent. Lukas Brenner
Fachzahnarzt für Kieferorthopädie (CH) (important information!)
(if there is enough space, please also write:
Eidg. dipl. Zahnarzt, Mitglied VZT und BFA)
(address:)
Felsenrainstrasse 9
8963 Wiesental
(telephone number:)
044 512 37 40
(if there is much space left, also fax number, but it is not mandatory:
044 512 37 41)
info@bisslinie-praxis.net
www.bisslinie-praxis.net
(If there is space left:
QR-code with the homepage-adress: www.bisslinie-praxis.net
and in the center of the QR-Code a little logo)

- It is important not to overload the card. Put in the optional parts only if it doesn't look overloaded or distribute them on the two sides.

Thank you for your designs. They are very nice. Please note that on the inner side the appointments will be printed as shown in the "appointment card.pdf". Please design a background that doesn't interfere with the Text and the QR-Codes. Thank you very much.

Target Market(s)

Orthodontist (Dentist)

Industry/Entity Type

It Professional

Contact Information for Business Card

Size: 85mm x 130mm
- Logo
- Text:
(address:)
Felsenrainstrasse 9
8963 Wiesental
(telephone number:)
044 512 37 40
044 512 37 41)
info@bisslinie-praxis.net
www.bisslinie-praxis.net
(If there is space left:

Font styles to use
Sans Serif

Colors

Designer to choose colors to be used in the design.

Requirements
Must have
• The designs and colors should be in harmony with the existing logo (uploaded).
• The font of the logo text is also uploaded. You don't need to use the same font, but the used fonts have to be in harmony with the font used in the logo.
• The colors used have to be in harmony with the logo.
• Size: 85mm x 130mm
• The appointment card will be folded vertically in the middle (folded size: 85mm x 65mm). Please design both outer sides.
• The appointments will be printed on the inner side (see uploaded "appointment card.pdf"). Please design the background on the inner side, but make it discreet.
• Following information have to be present:
• - Logo
• - Text:
• Kieferorthopädie Birkenhain
• Dr. med. dent. Lukas Brenner
• Fachzahnarzt für Kieferorthopädie (CH) (important information!)
• (if there is enough space, please also write:
• Eidg. dipl. Zahnarzt, Mitglied VZT und BFA)
• (address:)
• Felsenrainstrasse 9
• 8963 Wiesental
• (telephone number:)
• 044 512 37 40
• (if there is much space left, also fax number, but it is not mandatory:
• 044 512 37 41)
• info@bisslinie-praxis.net
• www.bisslinie-praxis.net
• (If there is space left:
• QR-code with the homepage-adress: www.bisslinie-praxis.net
• and in the center of the QR-Code a little logo)
• - It is important not to overload the card. Put in the optional parts only if it doesn't look overloaded or distribute them on the two sides.

```html
<!DOCTYPE html>
<html lang="de">
<head>
<meta charset="utf-8">
<title>Kieferorthopädie Birkenhain – Terminkarte</title>
<link rel="stylesheet" href="https://fonts.googleapis.com/css2?family=Open+Sans:wght@400;600;700&display=swap">
<style>
  :root {
    --backdrop: #b5b4b9;
    --sky: #00aeef;
    --navy: #1a1f6e;
    --brand-blue: #1565b8;
    --ink-grey: #55565a;
    --paper: #ffffff;
    --card-shadow: rgba(0, 0, 0, 0.45);
  }
  * { margin: 0; padding: 0; box-sizing: border-box; }
  html, body {
    width: 1200px; height: 900px; overflow: hidden;
    background: var(--backdrop);
    font-family: "Open Sans", Arial, sans-serif;
  }
  .canvas { position: relative; width: 1200px; height: 900px; }

  .card {
    position: absolute;
    background: var(--paper);
    box-shadow: 3px 4px 6px var(--card-shadow);
    overflow: hidden;
  }

  /* Outer side */
  .card-outer { left: 235px; top: 88px; width: 525px; height: 344px; }
  .contact-panel {
    position: absolute; left: 0; top: 0; width: 262px; height: 100%;
    background: var(--sky);
  }
  .contact-list {
    position: absolute; right: 24px; top: 206px;
    list-style: none; color: var(--paper);
    font-size: 14.5px; line-height: 17px; text-align: right;
  }
  .contact-list li { display: flex; justify-content: flex-end; align-items: center; gap: 6px; }
  .contact-list li.address-start { margin-top: 11px; }
  .contact-list svg { width: 11px; height: 11px; flex: none; }
  .contact-list .no-icon { padding-right: 17px; }

  .practice-block {
    position: absolute; left: 353px; top: 12px; height: 222px;
    writing-mode: vertical-rl; transform: rotate(180deg);
    white-space: nowrap;
  }
  .practice-name { color: var(--navy); font-weight: 700; font-size: 15px; line-height: 18px; }
  .practice-doctor { color: var(--ink-grey); font-size: 12.5px; line-height: 15px; }
  .practice-title { color: var(--ink-grey); font-size: 11px; line-height: 14px; }
  .practice-membership { color: var(--brand-blue); font-weight: 600; font-size: 9px; line-height: 16px; }

  .brand-mark {
    position: absolute; left: 350px; top: 246px; height: 72px;
    writing-mode: vertical-rl; transform: rotate(180deg);
    display: flex; align-items: center; gap: 5px;
    color: var(--navy); font-weight: 700; font-size: 13px;
  }
  .brand-mark .dot { width: 10px; height: 10px; border-radius: 50%; background: var(--sky); }

  /* Inner side */
  .card-inner { left: 403px; top: 461px; width: 527px; height: 343px; }
  .appointment-band {
    position: absolute; left: 0; top: 41px; width: 100%; height: 45px;
    background: var(--sky); color: var(--paper);
    font-weight: 600; font-size: 22px; line-height: 45px; text-align: center;
  }
  .appointment-fields {
    position: absolute; left: 44px; top: 160px;
    color: var(--ink-grey); font-size: 21px; white-space: nowrap;
  }
  .appointment-fields .gap { margin-left: 10px; }
  .weekday {
    position: absolute; top: 243px;
    display: flex; align-items: center; gap: 6px;
    color: var(--ink-grey); font-weight: 700; font-size: 17px;
  }
  .weekday.mon { left: 35px; }
  .weekday.tue { left: 112px; }
  .weekday.wed { left: 187px; }
  .weekday.thu { left: 266px; gap: 10px; }
  .weekday.fri { left: 349px; gap: 20px; }
  .weekday.sat { left: 425px; gap: 15px; }
  .checkbox { width: 14px; height: 14px; border: 1.5px solid var(--ink-grey); flex: none; }
</style>
</head>
<body>
<main class="canvas">

  <section class="card card-outer">
    <div class="contact-panel">
      <ul class="contact-list">
        <li>044 512 37 40
          <svg viewBox="0 0 12 12"><path fill="#fff" d="M1 4c0-2 2-3 5-3s5 1 5 3l-2 .5L8 3H4L3 4.5 1 4zm2 1h6l1.5 5h-9z"/></svg></li>
        <li>044 512 37 41)
          <svg viewBox="0 0 12 12"><path fill="#fff" d="M3 1h6v3H3zM1 4.5h10v5H9V8H3v1.5H1zM3.5 8.5h5V11h-5z"/></svg></li>
        <li>info@bisslinie-praxis.net
          <svg viewBox="0 0 12 12"><path fill="#fff" d="M1 2.5h10v7H1z"/><path fill="none" stroke="#00aeef" d="M1.5 3l4.5 3.5L10.5 3"/></svg></li>
        <li>www.bisslinie-praxis.net
          <svg viewBox="0 0 12 12"><circle cx="6" cy="6" r="5" fill="#fff"/><path fill="none" stroke="#00aeef" stroke-width=".8" d="M1 6h10M6 1c-2.5 3-2.5 7 0 10M6 1c2.5 3 2.5 7 0 10"/></svg></li>
        <li class="address-start">Felsenrainstrasse 9
          <svg viewBox="0 0 12 12"><path fill="#fff" d="M6 .5a3.5 3.5 0 0 1 3.5 3.5C9.5 7 6 11.5 6 11.5S2.5 7 2.5 4A3.5 3.5 0 0 1 6 .5z"/><circle cx="6" cy="4" r="1.3" fill="#00aeef"/></svg></li>
        <li class="no-icon">8963 Wiesental</li>
      </ul>
    </div>

    <div class="practice-block">
      <p class="practice-name">Kieferorthopädie Birkenhain</p>
      <p class="practice-doctor">Dr. med. dent. Lukas Brenner</p>
      <p class="practice-title">Fachzahnarzt für Kieferorthopädie (CH)</p>
      <p class="practice-membership">Eidg. dipl. Zahnarzt, Mitglied VZT und BFA</p>
    </div>

    <div class="brand-mark"><span class="dot"></span>Birkenhain</div>
  </section>

  <section class="card card-inner">
    <h2 class="appointment-band">Your Next Appointment on</h2>
    <p class="appointment-fields">Date : .................. <span class="gap">Time : ....................</span> <span class="gap">AM/PM</span></p>
    <span class="weekday mon"><span class="checkbox"></span>MON</span>
    <span class="weekday tue"><span class="checkbox"></span>TUE</span>
    <span class="weekday wed"><span class="checkbox"></span>WED</span>
    <span class="weekday thu"><span class="checkbox"></span>THU</span>
    <span class="weekday fri"><span class="checkbox"></span>FRI</span>
    <span class="weekday sat"><span class="checkbox"></span>SAT</span>
  </section>

</main>
</body>
</html>
```